" Atendimento em clínica especializada de otorrino na região do Ipiranga (São Paulo - SP), prestando atendimento médico, realizando exames e cirurgias na área. "

```html
<!DOCTYPE html>
<html lang="pt-BR">
<head>
<meta charset="UTF-8">
<title>Dr. Marcelo Andrade – Papel timbrado</title>
<link rel="stylesheet" href="https://fonts.googleapis.com/css2?family=Exo+2:wght@600;700&family=Open+Sans:wght@400;600&display=swap">
<style>
  :root {
    --backdrop: #e9e6e1;
    --paper: #ffffff;
    --brand-teal: #1f8fb3;
    --brand-navy: #1e3857;
    --text-dark: #2b2f36;
    --watermark: #f3f4f5;
  }
  * { box-sizing: border-box; margin: 0; padding: 0; }
  html, body {
    width: 1200px;
    height: 1200px;
    overflow: hidden;
    background: var(--backdrop);
  }
  .canvas {
    position: relative;
    width: 1200px;
    height: 1200px;
  }
  .letterhead {
    position: absolute;
    left: 170px;
    top: 67px;
    width: 860px;
    height: 1066px;
    background: var(--paper);
    box-shadow: 0 6px 24px rgba(0,0,0,0.12);
    overflow: hidden;
  }
  .letterhead__brand {
    position: absolute;
    top: 108px;
    left: 0;
    width: 100%;
    display: flex;
    flex-direction: column;
    align-items: center;
  }
  .brand__mark {
    width: 54px;
    height: 54px;
    border-radius: 50%;
    background: var(--brand-teal);
    margin-bottom: 12px;
  }
  .brand__name {
    font-family: "Exo 2", sans-serif;
    font-weight: 700;
    font-size: 27px;
    letter-spacing: 1.5px;
    color: var(--brand-navy);
    line-height: 1;
  }
  .brand__specialty {
    font-family: "Exo 2", sans-serif;
    font-weight: 600;
    font-size: 11.5px;
    letter-spacing: 3.6px;
    color: var(--brand-teal);
    margin-top: 7px;
  }
  .letterhead__watermark {
    position: absolute;
    left: 270px;
    top: 280px;
    width: 420px;
    height: 420px;
    border-radius: 50%;
    background: var(--watermark);
  }
  .letterhead__contact {
    position: absolute;
    left: 70px;
    top: 922px;
    list-style: none;
    font-family: "Open Sans", sans-serif;
    font-size: 13.5px;
    color: var(--text-dark);
  }
  .contact__item {
    display: flex;
    align-items: flex-start;
    gap: 9px;
    margin-bottom: 9px;
    line-height: 16px;
  }
  .contact__icon {
    flex: none;
    width: 16px;
    height: 16px;
  }
  .letterhead__tab {
    position: absolute;
    bottom: 0;
    left: 226px;
    width: 408px;
    height: 14px;
    background: var(--brand-teal);
    border-radius: 14px 14px 0 0;
  }
</style>
</head>
<body>
<div class="canvas">
  <section class="letterhead">
    <header class="letterhead__brand">
      <div class="brand__mark"></div>
      <div class="brand__name">DR. MARCELO ANDRADE</div>
      <div class="brand__specialty">OTORRINOLARINGOLOGIA</div>
    </header>

    <div class="letterhead__watermark" aria-hidden="true"></div>

    <ul class="letterhead__contact">
      <li class="contact__item">
        <svg class="contact__icon" viewBox="0 0 16 16" aria-hidden="true">
          <circle cx="8" cy="8" r="8" fill="var(--brand-teal)"/>
          <path d="M5.2 4.3l1.3-.3.8 1.8-.9.7c.4.9 1.1 1.6 2 2l.7-.9 1.8.8-.3 1.3c-3.1.1-5.5-2.3-5.4-5.4z" fill="#fff"/>
        </svg>
        <span>(00) 0000-0000</span>
      </li>
      <li class="contact__item">
        <svg class="contact__icon" viewBox="0 0 16 16" aria-hidden="true">
          <circle cx="8" cy="8" r="8" fill="var(--brand-teal)"/>
          <rect x="4" y="5.2" width="8" height="5.6" rx="0.6" fill="#fff"/>
          <path d="M4.3 5.6L8 8.3l3.7-2.7" fill="none" stroke="var(--brand-teal)" stroke-width="0.9"/>
        </svg>
        <span>contato@exemplo.com</span>
      </li>
      <li class="contact__item">
        <svg class="contact__icon" viewBox="0 0 16 16" aria-hidden="true">
          <circle cx="8" cy="8" r="8" fill="var(--brand-teal)"/>
        </svg>
        <span>www.exemplo.com.br</span>
      </li>
      <li class="contact__item">
        <svg class="contact__icon" viewBox="0 0 16 16" aria-hidden="true">
          <circle cx="8" cy="8" r="8" fill="var(--brand-teal)"/>
          <path d="M8 3.6a2.8 2.8 0 0 0-2.8 2.8c0 2.1 2.8 5.4 2.8 5.4s2.8-3.3 2.8-5.4A2.8 2.8 0 0 0 8 3.6z" fill="#fff"/>
          <circle cx="8" cy="6.4" r="1" fill="var(--brand-teal)"/>
        </svg>
        <span>rua exemplo, sl 000<br>cidade-UF, CEP: 00000-000</span>
      </li>
    </ul>

    <div class="letterhead__tab"></div>
  </section>
</div>
</body>
</html>
```